Local Restaurant Website Design

We are working with a Restaurant in California. They serve BBQ chicken, ribs, and other American cuisine. Plus catering.

Here are a few websites we found for inspiration:
https://www.marviegrillhouse.example
https://www.tarrowkitchen.example/home
https://brantellitrattoria.example
https://www.fondaverrel.example
https://www.korbins.example
https://elmiradorsmokesd.example
https://www.quepasotortilleria.example

Thank you for taking the time to consider designing a website for us. We are web developers based in Stockton, CA, USA. Most of our projects go through the same process. Understanding this process may help you win a project with us. We custom-code all of our websites in-house. We don’t have any requirements as to what tools you use for your design, but we ask that you follow these guidelines.

IMAGES:
If you use any images or icons in the design, we ask that you have a link to the asset so we can purchase the image/icon. Most of the designs we submit do not have the customer’s images on them unless they have some great images. Be creative; show us the feeling you are trying to portray with your image choices. Use any royalty-free site you choose. We subscribe to Vantrix and mainly use their images, but we can purchase images outside of Vantrix. PLEASE NOTE: we will not submit designs to clients with watermarks on the images.

FONTS:
We ask that you identify the fonts you’re using in the design. This can be done in a message if you want. We typically use Pelmor Type and Vantrix Type.

CONTENT:
We're always open to different content and ideas. We often submit designs with stock images so the client can see our vision. We typically take pictures after the website launch to use their images with our vision. Lorem Ipsum is fine for paragraphs, but we ask that you make the Headers with correct English. We want to be able to show the vision and identify the sections of the website.

INSPIRATION:
We typically add a couple of links in the brief of websites we like to help you get started in your design.

REVISIONS:
We do not often ask for revisions of the designs unless we see something in the design that may not appeal to the client. If there are slight changes that we want to make, we do that in the development process.

FEEDBACK:
We rarely give feedback on designs during the design process. We are working on many website projects and do not have the time to provide feedback. We usually respond if your request is well thought out and asks specific questions, but a note asking “feedback, please” usually goes unanswered.

```html
<!DOCTYPE html>
<html lang="en">
<head>
<meta charset="utf-8">
<title>Emberhen Grill – BBQ &amp; Catering</title>
<link href="https://fonts.googleapis.com/css2?family=Alegreya+Sans+SC:wght@700;800;900&family=Poppins:wght@400;500;600;700;800&display=swap" rel="stylesheet">
<style>
:root{
  --orange:#f0943a;
  --btn-text:#e0531c;
  --yellow:#ffd400;
  --white:#ffffff;
  --ink:#2b2b2b;
  --muted:#4a4a4a;
  --black:#000000;
  --hero-dark:#15171c;
}
*{margin:0;padding:0;box-sizing:border-box}
html,body{width:1200px;height:3323px;overflow:hidden}
body{position:relative;background:var(--white);font-family:'Poppins',sans-serif;color:var(--ink)}
.abs{position:absolute}
.heading{font-family:'Alegreya Sans SC',sans-serif;font-weight:900;color:var(--orange);letter-spacing:1px;line-height:1;white-space:nowrap}
.btn{position:absolute;display:flex;align-items:center;justify-content:center;background:var(--white);border:5px solid var(--yellow);color:var(--btn-text);font-weight:700;font-size:16px;text-transform:uppercase}
.photo{position:absolute}

/* hero */
.hero{left:0;top:0;width:1200px;height:597px;background:radial-gradient(ellipse at 15% 60%,#4a3326 0%,#221b18 45%,var(--hero-dark) 100%)}
.hero-panel{left:201px;top:148px;width:728px;height:449px;background:rgba(80,72,68,.55)}
.brand{display:flex;align-items:center;gap:8px;font-family:'Alegreya Sans SC',sans-serif;font-weight:900;color:var(--orange);text-transform:uppercase;white-space:nowrap}
.brand-mark{width:18px;height:18px;border-radius:50%;background:var(--orange)}
.top-brand{left:118px;top:76px;font-size:28px}
.nav-link{color:var(--white);font-weight:700;font-size:15px;text-transform:uppercase;letter-spacing:.3px;text-decoration:none}
.main-nav .nav-link{position:absolute;top:52px;white-space:nowrap}
.hero-title{left:280px;top:212px;font-size:80px;line-height:76px}
.hero-text{left:283px;top:374px;width:560px;color:var(--white);font-size:16px;line-height:27px}
.mascot{left:866px;top:108px;width:300px;height:562px;border-radius:40px;background:radial-gradient(ellipse at 45% 40%,#f4f4f4 0%,#e8a55a 45%,#8a2b1c 80%,rgba(90,30,20,0) 100%)}

/* about */
.about{left:0;top:597px;width:1200px;height:530px;background:linear-gradient(180deg,#0b0b0b 0%,#1e1410 45%,#3a2a20 80%,#1b1512 100%)}
.drumstick{left:168px;top:729px;width:180px;height:277px;border-radius:50% 50% 45% 45%;background:radial-gradient(ellipse at 50% 35%,#e0883e 0%,#b4521f 60%,rgba(120,50,20,0) 100%)}
.about-title{left:426px;top:697px;font-size:44px}
.about-text{left:426px;top:752px;width:662px;color:var(--white);font-size:16px;line-height:30px;text-align:justify}

/* menu */
.menu-title{left:0;width:1200px;top:1216px;text-align:center;font-size:44px}
.dish-name{font-family:'Alegreya Sans SC',sans-serif;font-weight:800;font-size:22px;color:var(--ink);white-space:nowrap}
.dish-price{font-family:'Alegreya Sans SC',sans-serif;font-weight:800;font-size:34px;color:var(--orange);margin-top:4px}
.dish-desc{font-size:14px;line-height:21px;color:var(--muted);margin-top:4px;width:180px}
.dots{display:flex;gap:3px}
.dots span{width:8px;height:8px;border-radius:50%;background:#b5b5b5}

/* catering */
.catering{left:0;top:1739px;width:1200px;height:399px;background:linear-gradient(120deg,#231d1a 0%,#3b2f28 40%,#1e1815 100%)}
.catering-title{left:0;width:1200px;top:1816px;text-align:center;font-size:44px}
.catering-text{left:310px;top:1894px;width:586px;text-align:center;color:var(--white);font-size:16px;line-height:27px}

/* gallery */
.gallery-title{left:0;width:1175px;top:2251px;text-align:center;font-size:44px}

/* footer */
.footer{left:0;top:2976px;width:1200px;height:347px;background:var(--black)}
.foot-brand{left:0;width:1200px;top:3070px;justify-content:center;font-size:40px}
.foot-nav .nav-link{position:absolute;top:3178px;white-space:nowrap}
.social{left:0;width:1200px;top:3225px;display:flex;justify-content:center;gap:28px}
.social span{width:14px;height:14px;border-radius:50%;background:var(--white)}
.foot-rule{left:0;top:3267px;width:1200px;height:1px;background:#555}
.copyright{left:0;width:1200px;top:3287px;text-align:center;color:var(--white);font-size:13px}
</style>
</head>
<body>

<!-- hero -->
<section class="abs hero" role="img" aria-label="Chicken pieces roasting on a dark grill"></section>
<div class="abs hero-panel"></div>
<div class="abs brand top-brand"><span class="brand-mark"></span>Emberhen Grill</div>
<nav class="main-nav">
  <a class="nav-link" style="left:372px">Home</a>
  <a class="nav-link" style="left:477px">About</a>
  <a class="nav-link" style="left:602px">Menu</a>
  <a class="nav-link" style="left:710px">Catering</a>
  <a class="nav-link" style="left:851px">Gallery</a>
  <a class="nav-link" style="left:984px">Contact Us</a>
</nav>

<!-- about background -->
<section class="abs about" role="img" aria-label="Flames rising behind a barbecue grill grate"></section>

<div class="abs mascot" role="img" aria-label="Cartoon chef mascot holding a carving fork"></div>
<h1 class="abs heading hero-title">Welcome to<br>Emberhen Grill</h1>
<p class="abs hero-text">On the other hand, we denounce with righteous indignation and dislike men who are so beguiled and demoralized by the charms of pleasure of the moment</p>
<a class="btn" style="left:283px;top:483px;width:163px;height:52px">Get Started</a>

<div class="abs drumstick" role="img" aria-label="Grilled chicken drumstick"></div>
<h2 class="abs heading about-title">About Us</h2>
<p class="abs about-text">Sed ut perspiciatis unde omnis iste natus error sit voluptatem accusantium doloremque laudantium, totam rem aperiam, eaque ipsa quae ab illo inventore veritatis et quasi architecto beatae vitae dicta sunt explicabo. Nemo enim ipsam voluptatem quia voluptas sit aspernatur aut odit aut fugit, sed quia consequuntur magni dolores eos qui ratione voluptatem sequi nesciunt. Neque porro quisquam est, qui dolorem ipsum quia dolor sit amet, consectetur, adipisci velit, sed quia non numquam eius modi tempora incidunt ut labore et dolore magnam</p>
<a class="btn" style="left:426px;top:984px;width:162px;height:52px">Read More</a>

<!-- menu -->
<h2 class="abs heading menu-title">Menu</h2>

<div class="abs menu-item" style="left:125px;top:1313px">
  <div class="dish-name">But I must explain</div>
  <div class="dish-price">$ 40</div>
  <p class="dish-desc">Sed ut perspiciatis unde omnis iste natus error</p>
</div>
<div class="photo" style="left:333px;top:1294px;width:249px;height:152px;background:linear-gradient(135deg,#c9cdd0,#b45a2a 50%,#7a2f16)" role="img" aria-label="Glazed chicken wings with dipping sauce"></div>

<div class="abs menu-item" style="left:609px;top:1313px">
  <div class="dish-name">But I must explain</div>
  <div class="dish-price">$ 80</div>
  <p class="dish-desc">Sed ut perspiciatis unde omnis iste natus error</p>
</div>
<div class="photo" style="left:817px;top:1294px;width:249px;height:152px;background:linear-gradient(90deg,#2a2420,#c87a3a 40%,#a9602c 70%,#2a2420)" role="img" aria-label="Grilled chicken breasts on a grill"></div>

<div class="abs menu-item" style="left:125px;top:1502px">
  <div class="dish-name">But I must explain</div>
  <div class="dish-price">$ 70</div>
  <p class="dish-desc">Sed ut perspiciatis unde omnis iste natus error</p>
</div>
<div class="photo" style="left:333px;top:1482px;width:249px;height:153px;background:linear-gradient(160deg,#3a1c14,#6a2a1a 50%,#2a1410)" role="img" aria-label="Rack of barbecue ribs"></div>

<div class="abs menu-item" style="left:609px;top:1502px">
  <div class="dish-name">But I must explain</div>
  <div class="dish-price">$ 30</div>
  <p class="dish-desc">Sed ut perspiciatis unde omnis iste natus error</p>
</div>
<div class="photo" style="left:817px;top:1482px;width:249px;height:153px;background:radial-gradient(circle at 62% 55%,#c77a36 0%,#8a5a30 35%,#ececec 60%)" role="img" aria-label="Roast chicken legs in a bowl"></div>

<div class="abs dots" style="left:586px;top:1694px"><span></span><span></span><span></span></div>

<!-- catering -->
<section class="abs catering" role="img" aria-label="Tongs over grilled meat"></section>
<h2 class="abs heading catering-title">Catering</h2>
<p class="abs catering-text">On the other hand, we denounce with righteous indignation and dislike men who are so beguiled and demoralized by the charms of pleasure of the moment</p>
<a class="btn" style="left:519px;top:2013px;width:161px;height:50px">Book Now</a>

<!-- gallery -->
<h2 class="abs heading gallery-title">Gallery</h2>
<div class="photo" style="left:110px;top:2352px;width:253px;height:245px;background:linear-gradient(150deg,#8a3416,#c8642a 50%,#3a1a10)" role="img" aria-label="Sticky glazed chicken wings"></div>
<div class="photo" style="left:392px;top:2352px;width:253px;height:245px;background:linear-gradient(160deg,#4f7a30,#d9a46a 45%,#b8743a)" role="img" aria-label="Grilled chicken breast with salad"></div>
<div class="photo" style="left:673px;top:2356px;width:417px;height:245px;background:linear-gradient(100deg,#262626,#c0652c 30%,#b45a26 65%,#262626)" role="img" aria-label="Roast chicken legs with rosemary"></div>
<div class="photo" style="left:111px;top:2628px;width:417px;height:245px;background:linear-gradient(120deg,#3a2a1c,#b87040 45%,#5a3a22)" role="img" aria-label="Chicken and pepper skewers"></div>
<div class="photo" style="left:551px;top:2628px;width:253px;height:245px;background:linear-gradient(140deg,#c55a1a,#8a3810 60%,#5a240c)" role="img" aria-label="Barbecue glazed chicken close-up"></div>
<div class="photo" style="left:833px;top:2628px;width:253px;height:245px;background:linear-gradient(150deg,#2a1a14,#c4562a 50%,#3a2218)" role="img" aria-label="Roast chicken with herbs"></div>
<div class="abs dots" style="left:586px;top:2930px"><span></span><span></span><span></span></div>

<!-- footer -->
<footer class="abs footer"></footer>
<div class="abs brand foot-brand"><span class="brand-mark"></span>Emberhen Grill</div>
<nav class="foot-nav">
  <a class="nav-link" style="left:243px">Home</a>
  <a class="nav-link" style="left:348px">About</a>
  <a class="nav-link" style="left:473px">Menu</a>
  <a class="nav-link" style="left:582px">Catering</a>
  <a class="nav-link" style="left:722px">Gallery</a>
  <a class="nav-link" style="left:855px">Contact Us</a>
</nav>
<div class="abs social" aria-label="Social links"><span></span><span></span><span></span><span></span><span></span></div>
<div class="abs foot-rule"></div>
<p class="abs copyright">© 2023&nbsp; EMBERHEN GRILL</p>

</body>
</html>
```